Tall Pine Advertising ad for electronic billboard

I need an ad made for an electronic billboard (13 feet x 26 Feet)(1024 x 480)
We own the billboard and want an ad to draw in customers.
Phone number: 250-317-4056
email: tbrask@tallpineadvertising.ca
I was thinking a Tall Pine swimming in the background with our email, phone number and company name Tall Pine in grey sitting above Advertising in white.
It can't be to busy, the less busy the ad is the better.

Target Market(s)

we are located in a oil patch town

Industry/Entity Type

Electronic

Requirements
Must have
• phone number
• your ad here
• email
• company name
Nice to have
• a shark

```html
<!DOCTYPE html>
<html lang="en">
<head>
<meta charset="utf-8">
<title>Tall Pine Advertising – Billboard Ad</title>
<link href="https://fonts.googleapis.com/css2?family=PT+Sans:wght@400;700&display=swap" rel="stylesheet">
<style>
  :root {
    --page: #ffffff;
    --brand-blue: #3549a3;
    --sky-top: #dcdcee;
    --sky-mid: #eeeef8;
    --board-white: #ffffff;
    --ink: #111111;
    --water-light: #e4e6ef;
    --water-mid: #b9bdcc;
    --shadow: rgba(0, 0, 0, 0.35);
  }
  * { box-sizing: border-box; margin: 0; padding: 0; }
  html, body {
    width: 1200px; height: 1000px; overflow: hidden;
    background: var(--page);
    font-family: "PT Sans", sans-serif;
  }
  .billboard {
    position: absolute; left: 141px; top: 286px;
    width: 935px; height: 437px;
    background: linear-gradient(to bottom, var(--sky-top) 0%, var(--sky-mid) 40%, var(--board-white) 78%);
    box-shadow: 2px 3px 6px var(--shadow);
    overflow: hidden;
  }
  .brand {
    position: absolute; left: 37px; top: 30px;
    display: flex; align-items: center; gap: 10px;
  }
  .brand-dot {
    width: 46px; height: 46px; border-radius: 50%;
    background: var(--brand-blue);
  }
  .brand-name {
    color: var(--brand-blue); font-size: 20px; font-weight: 700; line-height: 1.1;
    width: 110px;
  }
  .brand-label {
    position: absolute; left: 37px; top: 114px; width: 150px;
    text-align: center; color: var(--brand-blue); font-size: 17px;
  }
  .water-band {
    position: absolute; left: 4px; top: 140px; width: 931px; height: 150px;
    background: linear-gradient(to bottom, rgba(185,189,204,0) 0%, var(--water-mid) 30%, var(--water-light) 60%, rgba(228,230,239,0) 100%);
    opacity: 0.8;
  }
  .headline {
    position: absolute; left: 373px; top: 222px;
    color: var(--brand-blue); font-size: 72px; font-weight: 400;
    letter-spacing: 0.5px; white-space: nowrap;
  }
  .contact {
    position: absolute; left: 32px; display: flex; align-items: center;
    color: var(--ink); font-size: 29px; white-space: nowrap;
  }
  .contact-phone { top: 330px; left: 45px; gap: 26px; }
  .contact-email { top: 383px; gap: 8px; }
  .contact svg { display: block; }
</style>
</head>
<body>
  <main class="billboard">
    <div class="brand">
      <span class="brand-dot"></span>
      <span class="brand-name">Tall Pine Advertising</span>
    </div>
    <div class="brand-label">Tall Pine</div>

    <div class="water-band" role="img" aria-label="Splash of clear water flowing across the billboard"></div>

    <h1 class="headline">your Ad here</h1>

    <div class="contact contact-phone">
      <svg width="24" height="40" viewBox="0 0 24 40" aria-hidden="true">
        <rect x="1.5" y="1.5" width="21" height="37" rx="3" fill="none" stroke="var(--brand-blue)" stroke-width="3"/>
        <line x1="2" y1="31" x2="22" y2="31" stroke="var(--brand-blue)" stroke-width="2"/>
        <circle cx="12" cy="35" r="1.8" fill="var(--brand-blue)"/>
      </svg>
      <span>250-317-4056</span>
    </div>

    <div class="contact contact-email">
      <svg width="48" height="30" viewBox="0 0 48 30" aria-hidden="true">
        <rect x="0" y="0" width="48" height="30" fill="var(--brand-blue)"/>
        <polyline points="1,2 24,17 47,2" fill="none" stroke="#ffffff" stroke-width="2"/>
      </svg>
      <span>tbrask@tallpineadvertising.ca</span>
    </div>
  </main>
</body>
</html>
```